Webdesign für Gerüstbau Brenner
Zielgruppe
In der über 20-jährigen erfolgreichen Firmengeschichte ist die Firma Gerüstbau Brenner GmbH ein leistungsstarker und kompetenter Partner für Kunden im Raum Sachsen und Thüringen. Der Aktionsradius erstreckt sich auf ca. 100 km um die Stadt Glauchau OT Niederschindmaas herum. Das Unternehmen arbeitet ausschließlich mit Kolvex-Gerüsten.
Dafür stehen ca. 40.000 m² Kolvex-Sturm-Gerüst, ca. 4.000 m² Modulgerüst, Kassetten- und Planendächer, Treppenaufgänge und Nottreppen, Fahr- und Rollgerüste sowie weitere Sonderteile zur Verfügung.
Zielgruppe sind:
- Bau- und Dachdeckerfirmen,
- Handwerksbetriebe,
- Ingenieurbüros,
- Kommunen,
- Kirchen,
- landwirtschaftlichen Betriebe,
- Industrie
- und Privatpersonen
Aufgabenstellung
Unserem Auftraggeber gefällt ein großes Auftaktfoto gut, ansonsten ist er offen für ein modernes Layout.
- Layout als PSD
- Notwendige Bilder ausschließlich von Bildquell-Archiv.de
- Bitte nur die Startseite layouten
- blau des Logos und eine Zweitfarbe
- Slogan: Wir lösen Ihre Gerüstprobleme! Sprechen Sie mit uns!

```html
<!DOCTYPE html>
<html lang="de">
<head>
<meta charset="utf-8">
<title>Gerüstbau Brenner – Startseite</title>
<link href="https://fonts.googleapis.com/css2?family=Roboto:wght@400;500;700&family=Raleway:wght@500&display=swap" rel="stylesheet">
<style>
:root{
  --blue:#1b5d97;
  --blue-dark:#174f82;
  --green:#76b72a;
  --dark:#2b2b2b;
  --text:#555;
  --light:#f3f3f3;
  --white:#fff;
}
*{box-sizing:border-box;margin:0;padding:0}
html,body{width:1200px;height:2368px;overflow:hidden}
body{font-family:'Roboto',sans-serif;color:var(--text);background:var(--white);position:relative}
.abs{position:absolute}
/* header */
.header{position:absolute;left:0;top:0;width:1200px;height:100px;background:var(--white)}
.brand{position:absolute;left:235px;top:15px;display:flex;align-items:center;gap:14px}
.brand-mark{width:71px;height:71px;background:var(--blue)}
.brand-name{font-family:'Roboto',sans-serif;font-weight:500;font-size:13px;color:var(--blue);line-height:16px;width:120px}
.tagline{position:absolute;left:320px;top:35px;font-family:'Raleway',sans-serif;font-size:12.5px;color:var(--blue);line-height:16px}
.nav{position:absolute;top:52px;left:0;font-size:10.5px;color:#333}
.nav a{position:absolute;white-space:nowrap;text-decoration:none;color:#333;top:0}
.nav a.active{color:var(--green)}
.nav .caret{display:inline-block;width:5px;height:5px;border-right:1.2px solid #333;border-bottom:1.2px solid #333;transform:rotate(45deg);margin-left:7px;position:relative;top:-2px}
.btn-contact{position:absolute;left:879px;top:49px;width:86px;height:22px;border-radius:11px;background:var(--green);color:#fff;font-size:8.5px;font-weight:700;display:flex;align-items:center}
.btn-contact span{width:58px;text-align:center}
.btn-contact i{width:1px;height:16px;background:rgba(255,255,255,.5)}
.btn-contact svg{margin-left:7px}
/* hero */
.hero{position:absolute;left:0;top:100px;width:1200px;height:418px;background:linear-gradient(180deg,#5f87c0 0%,#a8c0de 40%,#c9d3dd 62%,#6a6660 78%,#3a3531 100%)}
.hero-title{position:absolute;right:0;background:var(--dark);color:#fff;font-size:31px;line-height:44px;padding:0 16px 0 21px;white-space:nowrap}
.hero-title em{font-style:normal;font-weight:700;color:var(--green)}
/* section title */
.tag{position:absolute;background:var(--green);color:#fff;font-weight:700;font-size:17px;height:31px;line-height:31px;padding:0 12px}
.tag:after{content:"";position:absolute;bottom:-6px;border-top:6px solid var(--green);border-left:6px solid transparent;border-right:6px solid transparent}
.tag.left:after{left:0;border-left:none;border-right:6px solid transparent}
.tag.center:after{left:50%;margin-left:-6px}
/* about */
.about-text{position:absolute;left:235px;top:622px;width:345px;font-size:10px;line-height:18.8px}
.btn-outline{position:absolute;left:235px;top:777px;width:106px;height:31px;border:2px solid var(--blue);border-radius:16px;color:var(--blue);font-size:10px;font-weight:700;display:flex;align-items:center;justify-content:center}
.about-visual{position:absolute;left:588px;top:551px;width:404px;height:267px;background:radial-gradient(ellipse at 50% 90%,#e4e4e4 0%,#fff 65%)}
/* services */
.services{position:absolute;left:0;top:852px;width:1200px;height:687px;background:var(--light)}
.lead{position:absolute;left:0;width:1200px;text-align:center;font-size:10px;line-height:18.8px}
.card{position:absolute;width:232px;background:#fff;box-shadow:0 1px 3px rgba(0,0,0,.08)}
.card .ph{width:232px}
.card h3{font-size:12px;font-weight:500;color:#333;text-align:center;line-height:56px}
.arrow{position:absolute;top:1228px}
.dots{position:absolute;left:586px;top:1458px;display:flex;gap:6px}
.dots i{width:6px;height:6px;border-radius:50%;background:var(--green)}
.dots i:first-child{background:var(--blue)}
/* news */
.news{position:absolute;width:232px;height:326px;background:#fff;box-shadow:0 1px 5px rgba(0,0,0,.12)}
.news .ph{height:135px}
.news h3{margin:25px 17px 0;font-size:12px;font-weight:500;color:#222;line-height:15px}
.news p{margin:13px 17px 0;font-size:9.2px;line-height:15.6px;color:#666}
.news a{display:block;margin:14px 17px 0;font-size:9.5px;font-weight:700;color:var(--blue);text-decoration:none}
/* footer */
.strip{position:absolute;left:0;top:2068px;width:1200px;height:24px;background:repeating-linear-gradient(90deg,#f3f3f3 0 24px,#ececec 24px 48px)}
.footer{position:absolute;left:0;top:2092px;width:1200px;height:224px;background:var(--blue);color:#fff}
.footer h4{position:absolute;top:48px;font-size:11.5px;font-weight:700}
.flist{position:absolute;top:80px;list-style:none;font-size:8.5px}
.flist li{height:25.7px;padding-left:12px;position:relative}
.flist li:before{content:"";position:absolute;left:0;top:3px;width:4px;height:4px;border-radius:50%;background:#fff}
.fitem{position:absolute;left:528px;font-size:8.5px;line-height:16px;display:flex;gap:9px}
.fitem svg{margin-top:3px;flex:none}
.bottom{position:absolute;left:0;top:2316px;width:1200px;height:52px;background:#fff;font-size:8.5px;color:#777}
</style>
</head>
<body>

<header class="header">
  <div class="brand"><div class="brand-mark"></div></div>
  <div class="tagline">Wir lösen auch<br>Ihre Gerüstprobleme!</div>
  <nav class="nav">
    <a class="active" style="left:505px">Startseite</a>
    <a style="left:578px">Leistungen<span class="caret"></span></a>
    <a style="left:657px">Unternehmen</a>
    <a style="left:746px">Aktuelles</a>
    <a style="left:818px">Karriere</a>
  </nav>
  <div class="btn-contact"><span>Kontakt</span><i></i>
    <svg width="13" height="13" viewBox="0 0 16 16" fill="none" stroke="#fff" stroke-width="1.6"><circle cx="8" cy="8" r="6.5"/><circle cx="8" cy="8" r="2.6"/><path d="M10.6 5.5v3.4c0 1.5 2.4 1.5 2.4-.9"/></svg>
  </div>
</header>
<div class="abs" style="left:235px;top:15px;width:71px;height:71px;background:var(--blue);display:flex;align-items:center;justify-content:center;color:#fff;font-size:8px;font-weight:700;text-align:center;line-height:10px">GERÜSTBAU<br>BRENNER</div>

<section class="hero" role="img" aria-label="Zwei Gerüstbauer mit Helmen tragen Gerüstteile auf einem Gerüststeg vor blauem Himmel mit Wolken">
  <div class="hero-title" style="top:145px;right:227px">ÜBER <em>30 JAHRE</em></div>
  <div class="hero-title" style="top:196px;right:227px">GERÜSTBAU BRENNER</div>
</section>

<div class="tag left" style="left:235px;top:569px">ÜBER UNS</div>
<p class="about-text">In der über 20-jährigen erfolgreichen Firmengeschichte waren und sind wir stets ein leistungsstarker und kompetenter Partner für unsere Kunden im Raum Sachsen und Thüringen. Unser Aktionsradius erstreckt sich auf ca. 100 km im Umkreis. Mit unserem im Jahresdurchschnitt 15-köpfigem Team sind wir in der Lage, die meisten im Gerüstbau geforderten Leistungen zu erbringen. Einen Einblick über von uns ausgeführte Arbeiten erhalten Sie auf der nachfolgenden Seite.</p>
<div class="btn-outline">Referenzen</div>
<div class="about-visual" role="img" aria-label="Freistehendes Gerüst mit Werbebanner der Firma"></div>

<section class="services">
  <div class="tag center" style="left:502px;top:53px">UNSERE LEISTUNGEN</div>
  <p class="lead" style="top:110px">Wir arbeiten ausschließlich mit Kolvex-Gerüsten.<br>Dafür stehen ca. 40.000 m² Kolvex-Sturm-Gerüst, ca. 4.000 m² Modulgerüst, Kassetten- und Planendächer,<br>Treppenaufgänge und Nottreppen, Fahr- und Rollgerüste sowie weitere Sonderteile zur Verfügung.</p>
  <p class="lead" style="top:185px">Für den Transport des Gerüstmaterials haben wir vier LKW, z.T. mit Ladekran, und einen<br>Transporter im Einsatz.</p>
</section>
<div class="card" style="left:235px;top:1104px"><div class="ph" style="height:251px;background:linear-gradient(180deg,#c8cbcd,#6e6a62 55%,#4d4a44)" role="img" aria-label="Eingerüstete historische Fassade"></div><h3>FASSADENGERÜSTE</h3></div>
<div class="card" style="left:485px;top:1104px"><div class="ph" style="height:251px;background:linear-gradient(180deg,#7a9fd8,#dfe3e6 45%,#8c8c84 90%)" role="img" aria-label="Gebäude mit Kassettendach und Planen"></div><h3>KASSETTENDÄCHER</h3></div>
<div class="card" style="left:735px;top:1104px"><div class="ph" style="height:251px;background:linear-gradient(160deg,#6b5c4a,#a88262 50%,#5a574f)" role="img" aria-label="Raumgerüst in einer Innenhalle"></div><h3>RAUMGERÜSTE</h3></div>
<svg class="arrow" style="left:176px" width="24" height="30" viewBox="0 0 24 30"><path d="M18 2 6 15l12 13" fill="none" stroke="#c8c8c8" stroke-width="5"/></svg>
<svg class="arrow" style="left:996px" width="24" height="30" viewBox="0 0 24 30"><path d="M6 2l12 13L6 28" fill="none" stroke="#8a9bab" stroke-width="5"/></svg>
<div class="dots"><i></i><i></i><i></i></div>

<div class="tag left" style="left:539px;top:1596px">AKTUELLES</div>
<article class="news" style="left:234px;top:1662px">
  <div class="ph" style="background:linear-gradient(180deg,#5b86c4,#9b8d80 70%,#7a5d48)" role="img" aria-label="Gerüst an einer Schlossfassade"></div>
  <h3>Schloss Lichtenstein in Sachsen -<br>Wir bauen das Gerüst!</h3>
  <p>Das Schloss Lichtenstein befindet sich in exponierter Lage auf dem Schlossberg in Lichtenstein und wird derzeit denkmal-schutzgerecht zu einem Schlosshotel mit Wellnesslandschaft umgebaut und saniert.</p>
  <a>mehr erfahren</a>
</article>
<article class="news" style="left:484px;top:1662px">
  <div class="ph" style="background:linear-gradient(90deg,#8a5c47,#d9b03a 45%,#9b8a75)" role="img" aria-label="Handwerker mit gelbem Helm und Werkzeuggürtel"></div>
  <h3>Neue engagierte Mitarbeiter<br>für das Jahr 2022 gesucht</h3>
  <p>Sie sind Gerüstbauer oder haben einen an-deren einschlägigen Bauberuf und möchten sich beruflich verändern? Dann rufen Sie bei uns an!&nbsp; Auch Gerüstbauhelfer sind herzlich willkommen, Sie werden hier angelernt.</p>
  <a>mehr erfahren</a>
</article>
<article class="news" style="left:735px;top:1662px">
  <div class="ph" style="background:linear-gradient(90deg,#c9a565,#a4a9ad 55%,#5a77a8)" role="img" aria-label="Eingerüstetes Haus am Marktplatz"></div>
  <h3>Unser letztes Projekt:<br>Auf dem Zwickauer Hauptmarkt</h3>
  <p>Lorem ipsum dolor sit amet, consetetur sadipscing elitr, sed diam nonumy eirmod tempor invidunt ut labore et dolore magna aliquyam erat, sed diam voluptua. At vero eos et accusam et justo duo dolores et...</p>
  <a>mehr erfahren</a>
</article>

<div class="strip"></div>
<footer class="footer">
  <h4 style="left:233px">UNSERE GERÜSTE</h4>
  <ul class="flist" style="left:240px"><li>Fassadengerüste</li><li>Kassettendächer</li><li>Spezialgerüste</li><li>Treppentürme</li></ul>
  <ul class="flist" style="left:346px"><li>für Kirchen &amp; Denkmälern</li><li>Fahrgerüste</li><li>Über uns</li><li>Karriere</li></ul>
  <h4 style="left:528px">KONTAKT</h4>
  <div class="fitem" style="top:80px;font-size:11px;font-weight:700"><svg width="10" height="10" viewBox="0 0 10 10"><rect width="10" height="10" rx="2" fill="#fff"/><path d="M3 2.5c-.5 2 1.5 4.5 4.5 5l.6-1.3-1.3-.7-.6.6C5 5.6 4.4 5 4 4.2l.6-.6-.6-1.3z" fill="#1b5d97"/></svg>03763-410527</div>
  <div class="fitem" style="top:105px"><svg width="11" height="9" viewBox="0 0 11 9"><path d="M5.5 0 11 4.5H9.5V9h-3V6h-2v3h-3V4.5H0z" fill="#fff"/></svg><span>Am Lindenhang 14<br>08397 Kerbenhain</span></div>
  <div class="fitem" style="top:145px"><svg width="10" height="10" viewBox="0 0 10 10" fill="none" stroke="#fff" stroke-width="1.3"><circle cx="5" cy="5" r="4"/><path d="M5 2.6V5h2"/></svg><span>Öffnungszeiten: 8:00 - 17:00 Uhr<br>Samstag von 8:00 - 14:0 Uhr</span></div>
  <div class="abs" style="left:746px;top:46px;font-size:20px;font-weight:400;color:#fff">Kolvex</div>
  <div class="abs" style="left:746px;top:81px;font-size:8.5px">Wir bauen mit dem Kolvex Gerüst-System</div>
  <div class="abs" style="left:746px;top:106px;font-size:8.5px">Datenschutz | Impressum</div>
  <div class="abs" style="left:748px;top:129px;display:flex;gap:10px"><i style="width:15px;height:15px;border-radius:50%;background:#fff"></i><i style="width:15px;height:15px;border-radius:50%;background:#fff"></i><i style="width:15px;height:15px;border-radius:50%;background:#fff"></i></div>
</footer>
<div class="bottom">
  <div class="abs" style="left:235px;top:12px;width:26px;height:26px;background:#dce6f0"></div>
  <div class="abs" style="left:273px;top:20px">Die Präqualifizierung erfolgte unter der Registriernummer 110.004172</div>
  <div class="abs" style="right:234px;top:20px">© 2022 Gerüstbau Brenner GmbH</div>
</div>
</body>
</html>
```